Business card and logo designs

We are looking to create a cool and trendy image for the company, some thing what quince has. We already have a logo, but we can reconsider a new logo.

Volturo provides a new kind of web service for businesses to take appointments using web and mobile. Usually a customer needs to call or check several times. Volturo solves this trouble. Our service refills cancellations quickly and automatically plus reduces no-shows. On top of that, our analytical tools give deep business and customer insights to increase revenue.

Phone bookings and cancellations are frustrating, time-consuming and expensive.It can take hours to book a 20 min appointment for e.g. with your doctor. When customers don’t find a suitable time, they need to call or check online again and again. Volturo turn the tables and enables your doctor to get back to you with appointment of your choice,automatically. It refills cancellations quickly and automatically. Volutro did not invent a booking system, like Quince did not invest a mobile phone. However, we make it mobile, intelligent and useful.

Volturo identity should present a change, the same one which quince brought to mobile. Despite the fact that booking systems has been around for 2 decades, we change the game.

We want to communicate that we are saving time for consumers and businesses in an an innovative way and helping businesses to improve revenue.
Updates

Reason: We want more design entries.

Contents of the business card....

But we want the empty template so when new people join, we use the same.

Tomas Lindqvel

+358-402759130

Founder & CEO 

tomas.lindqvel@volturo.example

 Volturo Solutions Oy

Helsinki, Finland

www.volturo.example

All,

We have to get ideas about a new logo. New business card is not enough.

Reason: More designs needed...

Reason: We have got very few good designs so far.

Reason: Need a bite more time... our creative director was busy

Target Market(s)

Most developed countries

Industry/Entity Type

Doctor

Requirements
Must have
• Color orange and green....
Should not have
• Should not have the obvious things... more intelligent design...

```html
<!DOCTYPE html>
<html lang="en">
<head>
<meta charset="utf-8">
<title>Volturo business card</title>
<link rel="stylesheet" href="https://fonts.googleapis.com/css2?family=Roboto:ital,wght@0,400;0,700;1,400;1,700&family=Roboto+Condensed:wght@400&display=swap">
<style>
  :root {
    --backdrop: #141414;
    --card-white: #ffffff;
    --card-grey-light: #f7f7f7;
    --card-grey-dark: #dcdcdc;
    --orange: #f47b20;
    --blue: #4f7fd0;
    --ink-dark: #4a4a4a;
    --ink-mid: #6a6a6a;
    --ink-soft: #8a8a8a;
    --rule: #9a9a9a;
  }
  * { margin: 0; padding: 0; box-sizing: border-box; }
  html, body { width: 1097px; height: 1200px; overflow: hidden; }
  body { background: var(--backdrop); position: relative; font-family: "Roboto", Arial, sans-serif; }

  .card { position: absolute; overflow: hidden; }
  .card--front { left: 201px; top: 133px; width: 678px; height: 431px; background: var(--card-white); }
  .card--back {
    left: 198px; top: 648px; width: 685px; height: 401px;
    background: radial-gradient(ellipse at 62% 18%, var(--card-white) 0%, var(--card-grey-light) 40%, var(--card-grey-dark) 100%);
  }

  .accent-bar {
    position: absolute; left: 0; top: 133px; width: 247px; height: 23px;
    background: var(--orange); border-radius: 0 12px 12px 0;
  }

  .person { position: absolute; left: 45px; top: 167px; display: inline-block; text-align: right; }
  .person__name { font-size: 29px; font-style: italic; line-height: 1; letter-spacing: 0.3px; white-space: nowrap; }
  .person__first { font-weight: 700; color: var(--ink-dark); }
  .person__last { font-weight: 400; color: var(--orange); }
  .person__role { font-size: 13px; color: var(--ink-mid); margin-top: 2px; letter-spacing: 0.4px; }

  .contact {
    position: absolute; list-style: none;
    font-family: "Roboto Condensed", "Arial Narrow", sans-serif;
    text-transform: uppercase; color: var(--ink-mid);
  }
  .card--front .contact { left: 38px; top: 266px; font-size: 13.5px; line-height: 19.8px; }
  .card--back .contact { left: 21px; top: 240px; font-size: 13px; line-height: 15.8px; color: var(--ink-soft); }

  .brand { position: absolute; display: flex; align-items: center; gap: 10px; }
  .brand__dot { width: 28px; height: 28px; border-radius: 50%; background: var(--blue); flex: none; }
  .brand__name { font-family: "Roboto", Arial, sans-serif; font-weight: 700; color: var(--orange); line-height: 1; }
  .card--front .brand { left: 352px; top: 205px; }
  .card--front .brand__name { font-size: 46px; }
  .card--back .brand { left: 405px; top: 36px; }
  .card--back .brand__name { font-size: 38px; }
  .card--back .brand__dot { width: 24px; height: 24px; }

  .back-name {
    position: absolute; right: 70px; top: 124px;
    font-size: 18px; font-style: italic; color: #222; white-space: nowrap;
  }
  .back-name strong { font-weight: 700; }

  .divider { position: absolute; left: 46px; top: 178px; width: 602px; height: 1px; background: var(--rule); }

  .back-web {
    position: absolute; left: 21px; top: 198px;
    font-family: "Roboto Condensed", "Arial Narrow", sans-serif;
    font-size: 13px; color: var(--ink-soft); text-transform: uppercase;
  }
</style>
</head>
<body>

<section class="card card--front" aria-label="Business card front">
  <div class="accent-bar"></div>
  <div class="person">
    <p class="person__name"><span class="person__first">TOMAS</span> <span class="person__last">LINDQVEL</span></p>
    <p class="person__role">manager</p>
  </div>
  <ul class="contact">
    <li>www.volturo.example</li>
    <li>Volturo Solutions Oy</li>
    <li>Helsinki, Finland</li>
    <li>tomas.lindqvel@volturo.example</li>
    <li>+358-402759130</li>
    <li>(555) 555 - 6789 (work)</li>
    <li>(555) 555 - 1234 (cell)</li>
  </ul>
  <div class="brand">
    <span class="brand__dot"></span>
    <span class="brand__name">Volturo</span>
  </div>
</section>

<section class="card card--back" aria-label="Business card back">
  <div class="brand">
    <span class="brand__dot"></span>
    <span class="brand__name">Volturo</span>
  </div>
  <p class="back-name"><strong>TOMAS</strong> LINDQVEL</p>
  <div class="divider"></div>
  <p class="back-web">www.volturo.example</p>
  <ul class="contact">
    <li>Volturo Solutions Oy</li>
    <li>Helsinki, Finland</li>
    <li>tomas.lindqvel@volturo.example</li>
    <li>+358-402759130</li>
    <li>(555) 555 - 6789 (work)</li>
    <li>(555) 555 - 1234 (cell)</li>
  </ul>
</section>

</body>
</html>
```